Visitenkarten-Design für Gesundheits- und Ernährungsberaterin
Zielgruppe
Ich bin Gesundheit und Ernährungsberaterin
Zielgruppe sind chronisch Kranke und Gesundheitsbewusste Personen
Aufgabenstellung
Schlichtes aber direkt erkennbares Design.
Mahl mit Maß , Gesundheit und Ernährungsberatung ( gut lesbar , elegant)
Marlene Obruk-Feistinger ( nicht so groß )
Grau ; Grün Töne und gerne etwas rosa
Infos wie Adresse und E-Mail vielleicht in jeweilige Blöcke am unteren Rand

```html
<!DOCTYPE html>
<html lang="de">
<head>
<meta charset="utf-8">
<title>Visitenkarten – Marlene Obruk-Feistinger</title>
<link href="https://fonts.googleapis.com/css2?family=Montserrat:ital,wght@0,400;0,500;0,700;1,400&display=swap" rel="stylesheet">
<style>
  :root {
    --grey-card: #646464;
    --text-grey: #555555;
    --green: #8ed660;
    --pink: #df8585;
    --paper: #ffffff;
    --sheet: #ffffff;
  }
  * { margin: 0; padding: 0; box-sizing: border-box; }
  html, body { width: 861px; height: 1200px; overflow: hidden; background: var(--sheet); }
  body { position: relative; font-family: "Montserrat", Arial, sans-serif; color: var(--text-grey); }

  .card {
    position: absolute;
    width: 336px;
    height: 220px;
    overflow: hidden;
    box-shadow: 3px 4px 8px rgba(0,0,0,0.28);
  }
  .card::before {
    content: "";
    position: absolute;
    left: 0; top: 0; bottom: 0;
    width: 10px;
    background: var(--accent);
  }
  .card--front { left: 67px; background: var(--grey-card); }
  .card--back { left: 438px; background: var(--paper); }
  .accent-green { --accent: var(--green); }
  .accent-pink { --accent: var(--pink); }

  .row-1 { top: 89px; }
  .row-2 { top: 353px; }
  .row-3 { top: 615px; }
  .row-4 { top: 866px; }

  .brand-mark {
    position: absolute;
    display: flex;
    align-items: center;
    gap: 7px;
    color: var(--green);
    font-weight: 700;
    white-space: nowrap;
  }
  .brand-mark .dot { border-radius: 50%; background: var(--green); flex: none; }
  .card--front .brand-mark { left: 5px; right: 0; top: 64px; justify-content: center; font-size: 30px; }
  .card--front .brand-mark .dot { width: 16px; height: 16px; }
  .card--back .brand-mark { right: 9px; top: 36px; font-size: 17px; gap: 5px; }
  .card--back .brand-mark .dot { width: 10px; height: 10px; }

  .tagline {
    position: absolute;
    color: var(--pink);
    font-style: italic;
    font-weight: 400;
    letter-spacing: 0.08em;
    text-transform: uppercase;
    white-space: nowrap;
  }
  .card--front .tagline { left: 5px; right: 0; top: 161px; text-align: center; font-size: 12.5px; }
  .card--back .tagline { right: 9px; top: 94px; font-size: 9.5px; }

  .person { position: absolute; left: 19px; top: 138px; text-transform: uppercase; }
  .person-name { font-weight: 700; font-size: 10.3px; letter-spacing: 0.01em; line-height: 1.1; }
  .person-role { font-size: 6.4px; letter-spacing: 0.02em; line-height: 1.2; }

  .address, .contact {
    position: absolute;
    font-size: 8.4px;
    line-height: 10.5px;
    text-transform: uppercase;
    white-space: nowrap;
  }
  .address { left: 19px; top: 192px; }
  .contact { right: 9px; top: 181px; }
  .contact li { list-style: none; display: flex; align-items: center; gap: 4px; }
  .contact svg { width: 8px; height: 8px; color: var(--icon, var(--text-grey)); flex: none; }
  .icons-green { --icon: var(--green); }
  .icons-pink { --icon: var(--pink); }
</style>
</head>
<body>
<svg width="0" height="0" style="position:absolute">
  <defs>
    <symbol id="icon-phone" viewBox="0 0 16 16"><path fill="currentColor" d="M3.6 1.2l2.3 2.6-1.3 2a9 9 0 0 0 5.6 5.6l2-1.3 2.6 2.3-1.5 2.3C7.2 14.6 1.4 8.8 1.3 2.7z"/></symbol>
    <symbol id="icon-mobile" viewBox="0 0 16 16"><path fill="currentColor" d="M8 1l6 7-6 7-6-7z"/></symbol>
    <symbol id="icon-mail" viewBox="0 0 16 16"><path fill="currentColor" d="M1 3h14v10H1z"/><path fill="none" stroke="#fff" stroke-width="1.3" d="M1.5 3.6L8 9l6.5-5.4M1.5 12.5L6 8M14.5 12.5L10 8"/></symbol>
  </defs>
</svg>

<!-- Row 1 -->
<section class="card card--front accent-green row-1">
  <div class="brand-mark"><span class="dot"></span>Grünzeit</div>
  <p class="tagline">Mahl mit Maß.</p>
</section>
<section class="card card--back accent-green row-1">
  <div class="brand-mark"><span class="dot"></span>Grünzeit</div>
  <p class="tagline">Mahl mit Maß.</p>
  <div class="person"><p class="person-name">Marlene Obruk-Feistinger</p><p class="person-role">Gesundheits- und Ernährungsberaterin</p></div>
  <p class="address">Lindenweg 4<br>24799 Meezen</p>
  <ul class="contact">
    <li><svg><use href="#icon-phone"/></svg>04331 / 724 19 06</li>
    <li><svg><use href="#icon-mobile"/></svg>0152 / 38 71 20 55</li>
    <li><svg><use href="#icon-mail"/></svg>beratung-mof@posteo.de</li>
  </ul>
</section>

<!-- Row 2 -->
<section class="card card--front accent-pink row-2">
  <div class="brand-mark"><span class="dot"></span>Grünzeit</div>
  <p class="tagline">Mahl mit Maß.</p>
</section>
<section class="card card--back accent-pink row-2">
  <div class="brand-mark"><span class="dot"></span>Grünzeit</div>
  <p class="tagline">Mahl mit Maß.</p>
  <div class="person"><p class="person-name">Marlene Obruk-Feistinger</p><p class="person-role">Gesundheits- und Ernährungsberaterin</p></div>
  <p class="address">Lindenweg 4<br>24799 Meezen</p>
  <ul class="contact">
    <li><svg><use href="#icon-phone"/></svg>04331 / 724 19 06</li>
    <li><svg><use href="#icon-mobile"/></svg>0152 / 38 71 20 55</li>
    <li><svg><use href="#icon-mail"/></svg>beratung-mof@posteo.de</li>
  </ul>
</section>

<!-- Row 3 -->
<section class="card card--front accent-green row-3">
  <div class="brand-mark"><span class="dot"></span>Grünzeit</div>
  <p class="tagline">Mahl mit Maß.</p>
</section>
<section class="card card--back accent-green icons-green row-3">
  <div class="brand-mark"><span class="dot"></span>Grünzeit</div>
  <p class="tagline">Mahl mit Maß.</p>
  <div class="person"><p class="person-name">Marlene Obruk-Feistinger</p><p class="person-role">Gesundheits- und Ernährungsberaterin</p></div>
  <p class="address">Lindenweg 4<br>24799 Meezen</p>
  <ul class="contact">
    <li><svg><use href="#icon-phone"/></svg>04331 / 724 19 06</li>
    <li><svg><use href="#icon-mobile"/></svg>0152 / 38 71 20 55</li>
    <li><svg><use href="#icon-mail"/></svg>beratung-mof@posteo.de</li>
  </ul>
</section>

<!-- Row 4 -->
<section class="card card--front accent-pink row-4">
  <div class="brand-mark"><span class="dot"></span>Grünzeit</div>
  <p class="tagline">Mahl mit Maß.</p>
</section>
<section class="card card--back accent-pink icons-pink row-4">
  <div class="brand-mark"><span class="dot"></span>Grünzeit</div>
  <p class="tagline">Mahl mit Maß.</p>
  <div class="person"><p class="person-name">Marlene Obruk-Feistinger</p><p class="person-role">Gesundheits- und Ernährungsberaterin</p></div>
  <p class="address">Lindenweg 4<br>24799 Meezen</p>
  <ul class="contact">
    <li><svg><use href="#icon-phone"/></svg>04331 / 724 19 06</li>
    <li><svg><use href="#icon-mobile"/></svg>0152 / 38 71 20 55</li>
    <li><svg><use href="#icon-mail"/></svg>beratung-mof@posteo.de</li>
  </ul>
</section>
</body>
</html>
```